Brantley Water Taxi and Transport

Need to redesign our business cards to relay that we do freight logistics and water taxi service. We also work with gov. agencies doing environmental clean up, oil spill response, remote site construction and work with many of the air taxi and helicopter services on Brantley Island. Out website is www.brantleywatertaxi-example.com to get a better idea of what we do.

Contact Information for Business Card

I have a previous business card but it just has the logo on the front, and a sunset picture on the back with the contact info. It does not relay what we do and what we can help with. I like a simple straight forward design over a busy one.

Colors
3176b5
0455a3
cfdfed

Requirements
Must have
• logo, email, website, phone number

```html
<!DOCTYPE html>
<html lang="en">
<head>
<meta charset="utf-8">
<title>Brantley Water Taxi and Transport – Business Card</title>
<link href="https://fonts.googleapis.com/css2?family=Bebas+Neue&family=Didact+Gothic&display=swap" rel="stylesheet">
<style>
  :root {
    --navy: #1a4698;
    --sky: #00b4e6;
    --mountain: #5ab4e0;
    --mist: #cfe6f5;
    --paper: #ffffff;
    --ink-dark: #1c1c1c;
    --backdrop: #5e5e5e;
    --ink-light: #ffffff;
  }
  html, body {
    margin: 0;
    padding: 0;
    width: 1200px;
    height: 1200px;
    overflow: hidden;
    background: var(--backdrop);
  }
  .canvas {
    position: relative;
    width: 1200px;
    height: 1200px;
  }
  .card {
    position: absolute;
    overflow: hidden;
  }
  .card-front {
    left: 269px;
    top: 170px;
    width: 662px;
    height: 379px;
    background: var(--paper);
  }
  .card-front .edge-bands {
    position: absolute;
    inset: 0;
    width: 100%;
    height: 100%;
  }
  .scene-artwork {
    position: absolute;
    left: 170px;
    top: 54px;
    width: 336px;
    height: 152px;
    border-radius: 6px;
    background: linear-gradient(180deg, var(--mist) 0%, var(--mountain) 100%);
  }
  .wordmark {
    position: absolute;
    left: 0;
    right: 0;
    top: 222px;
    text-align: center;
    font-family: "Didact Gothic", sans-serif;
    font-weight: 400;
  }
  .wordmark-name {
    display: block;
    font-size: 62px;
    line-height: 1;
    letter-spacing: 3px;
    text-transform: uppercase;
    color: var(--navy);
  }
  .wordmark-tagline {
    display: block;
    margin-top: 6px;
    font-size: 27px;
    letter-spacing: 1.5px;
    color: var(--ink-dark);
  }
  .card-back {
    left: 268px;
    top: 642px;
    width: 665px;
    height: 382px;
    background: var(--navy);
  }
  .divider {
    position: absolute;
    top: 86px;
    width: 3px;
    height: 210px;
    background: var(--ink-light);
  }
  .divider-left { left: 86px; }
  .divider-right { left: 567px; }
  .contact-list {
    position: absolute;
    left: 126px;
    top: 84px;
    margin: 0;
    padding: 0;
    list-style: none;
  }
  .contact-item {
    display: flex;
    align-items: center;
    height: 60px;
    margin-bottom: 16px;
  }
  .contact-icon {
    width: 60px;
    height: 60px;
    flex: none;
  }
  .contact-text {
    margin-left: 14px;
    font-family: "Bebas Neue", sans-serif;
    font-size: 26px;
    letter-spacing: 0;
    color: var(--ink-light);
    white-space: nowrap;
  }
</style>
</head>
<body>
<main class="canvas">

  <section class="card card-front" aria-label="Business card front">
    <svg class="edge-bands" viewBox="0 0 828 474" preserveAspectRatio="none" aria-hidden="true">
      <path fill="var(--navy)" d="M0,0 L72,0 C62,200 34,380 0,474 Z"/>
      <path fill="var(--sky)" d="M72,0 L106,0 C100,200 64,380 6,474 L0,474 C34,380 62,200 72,0 Z"/>
      <path fill="var(--sky)" d="M828,0 C760,110 726,300 722,474 L752,474 C756,300 790,120 828,14 Z"/>
      <path fill="var(--navy)" d="M828,14 C790,120 756,300 752,474 L828,474 Z"/>
    </svg>
    <div class="scene-artwork" role="img" aria-label="Illustration of a work boat on waves in front of mountains and a rising sun"></div>
    <div class="wordmark">
      <span class="wordmark-name">Brantley</span>
      <span class="wordmark-tagline">Water Taxi &amp; Transport</span>
    </div>
  </section>

  <section class="card card-back" aria-label="Business card back">
    <span class="divider divider-left"></span>
    <span class="divider divider-right"></span>
    <ul class="contact-list">
      <li class="contact-item">
        <svg class="contact-icon" viewBox="0 0 60 60" aria-hidden="true">
          <circle cx="30" cy="30" r="28" fill="none" stroke="#fff" stroke-width="2"/>
          <path fill="#fff" d="M15,26 C15,17 45,17 45,26 L45,29 L38,29 L38,25 L22,25 L22,29 L15,29 Z"/>
          <path fill="#fff" d="M22,29 L38,29 L44,41 L16,41 Z"/>
          <circle cx="30" cy="34" r="3.5" fill="var(--navy)"/>
        </svg>
        <span class="contact-text">907-555-0142</span>
      </li>
      <li class="contact-item">
        <svg class="contact-icon" viewBox="0 0 60 60" aria-hidden="true">
          <circle cx="30" cy="30" r="28" fill="none" stroke="#fff" stroke-width="2"/>
          <text x="30" y="40" text-anchor="middle" font-family="Didact Gothic, sans-serif" font-size="30" fill="#fff">@</text>
        </svg>
        <span class="contact-text">brantleywatertaxi@example.com</span>
      </li>
      <li class="contact-item">
        <svg class="contact-icon" viewBox="0 0 60 60" aria-hidden="true">
          <circle cx="30" cy="30" r="28" fill="none" stroke="#fff" stroke-width="2"/>
          <g fill="none" stroke="#fff" stroke-width="2">
            <circle cx="30" cy="30" r="18"/>
            <ellipse cx="30" cy="30" rx="8" ry="18"/>
            <line x1="30" y1="12" x2="30" y2="48"/>
            <line x1="12" y1="30" x2="48" y2="30"/>
            <path d="M15,21 H45 M15,39 H45"/>
          </g>
        </svg>
        <span class="contact-text">www.brantleywatertaxi-example.com</span>
      </li>
    </ul>
  </section>

</main>
</body>
</html>
```